Packaging Design job - Product : Supplement for Travel Sickness

We need a packaging design for a travel sickness supplement called "VOLUMAR"

VOLUMAR It is a dietary supplement based on ginger which has properties fighting against motion sickness.

Ginger is a root used for many years for its beneficial effects on health. In addition to its stimulating and toning properties which help to resist fatigue, ginger is used as an adjuvant in case of nausea, vomiting and motion sickness. Ideal for pregnant women to combat certain disadvantages of pregnancy.

This product will be in blister form of 30 capsules. We need for this a packaging design for the box.Dimensions: 100 * 20 * 200 mm

We would like to see clean, modern and fresh designs.This should give the impression of professional products of pharmaceutical quality. You will also find attached the logo of our company.Ps : You can change the color of the logo

Mention to put on the box :

• Produit en France: Laboratoire KRANIVO, 24 Rue des Lavandières 37410 BRÉCHAL
• Distribué au Maroc: LUMORAXIN 14 rue Oumaima Tazrouti 30050 FEZ MAROC
• Complément alimentaire, ce n'est pas un médicament
• Voie orale
• Tenir hors de portée des enfants
• Respectez la dose recommandée
• Ce produit ne remplace pas une alimentation variée

Mode d'utilisation (How to use) :

2 à 3 gélules 30 min avant de prendre le véhicule de transport
1 gélule par jour en cas de cure

Font styles to use
Serif
Sans Serif
Script

Requirements
Should not have
• Sales and other "must buy" "guaranteed" etc

```html
<!DOCTYPE html>
<html lang="en">
<head>
<meta charset="utf-8">
<title>VOLUMAR – Dietary Supplement Box</title>
<link rel="stylesheet" href="https://fonts.googleapis.com/css2?family=Montserrat:wght@600;800&family=Open+Sans:wght@300;400&family=Courier+Prime:wght@700&display=swap">
<style>
  :root {
    --backdrop: #e9e9e9;
    --box: #f1f1f1;
    --ink-grey: #5f6062;
    --ink-dark: #1d1d1d;
    --band-yellow: #e2da4a;
    --seal-green: #7cc243;
    --ginger-light: #f1e2b8;
    --ginger-mid: #e2c98f;
  }
  * { margin: 0; padding: 0; box-sizing: border-box; }
  html, body {
    width: 1200px; height: 1200px; overflow: hidden;
    background: var(--backdrop);
  }
  .box-front {
    position: absolute; left: 360px; top: 120px;
    width: 480px; height: 960px;
    background: var(--box);
    box-shadow: 0 0 0 1px #dcdcdc;
    overflow: hidden;
  }
  .brand {
    position: absolute; top: 58px; left: 0; width: 100%;
    text-align: center;
    font-family: "Montserrat", sans-serif; font-weight: 800;
    font-size: 22px; letter-spacing: 0.5px;
    color: var(--ink-dark);
  }
  .product-name {
    position: absolute; top: 276px; left: 0; width: 100%;
    text-align: center;
    font-family: "Montserrat", sans-serif; font-weight: 600;
    font-size: 74px; letter-spacing: 0; line-height: 1;
    color: var(--ink-grey);
    padding-left: 16px;
  }
  .product-type {
    position: absolute; top: 368px; left: 0; width: 100%;
    text-align: center;
    font-family: "Open Sans", sans-serif; font-weight: 300;
    font-size: 35px; line-height: 1;
    color: var(--ink-grey);
    padding-left: 12px;
  }
  .rule {
    position: absolute; left: 63px; width: 366px; height: 1.5px;
    background: var(--ink-grey);
  }
  .rule--title { top: 413px; }
  .claim-band {
    position: absolute; top: 506px; left: 0; width: 100%; height: 143px;
    background: var(--band-yellow);
    font-family: "Courier Prime", monospace; font-weight: 700;
    color: var(--ink-dark); text-align: center;
  }
  .claim-band .use {
    position: absolute; top: 31px; left: 0; width: 100%;
    font-size: 15.5px; line-height: 20px; padding-left: 24px;
  }
  .claim-band .rule { top: 82px; background: var(--ink-dark); height: 1px; }
  .claim-band .audience {
    position: absolute; top: 93px; left: 0; width: 100%;
    font-size: 15.5px; padding-left: 12px;
  }
  .ginger-visual {
    position: absolute; left: 214px; top: 714px; width: 238px; height: 184px;
    border-radius: 6px;
    background: linear-gradient(160deg, var(--ginger-light), var(--ginger-mid));
  }
  .organic-seal {
    position: absolute; left: 153px; top: 708px; width: 116px; height: 116px;
    border-radius: 50%;
    border: 3px solid var(--seal-green);
    background: var(--box);
  }
  .count {
    position: absolute; left: 18px; top: 840px;
    font-family: "Open Sans", sans-serif; font-weight: 400;
    font-size: 68px; line-height: 1; color: var(--ink-grey);
  }
  .count-unit {
    position: absolute; left: 14px; top: 918px;
    font-family: "Open Sans", sans-serif; font-weight: 400;
    font-size: 14px; color: var(--ink-grey);
  }
  .base-tag {
    position: absolute; left: 284px; top: 913px; width: 166px; height: 26px;
    border: 1.5px solid var(--ink-grey);
    font-family: "Open Sans", sans-serif; font-weight: 400;
    font-size: 14px; line-height: 23px; text-align: center;
    color: var(--ink-grey);
  }
</style>
</head>
<body>
  <main class="box-front">
    <div class="brand">LUMORAXIN</div>

    <h1 class="product-name">VOLUMAR</h1>
    <p class="product-type">DIETARY SUPPLEMENT</p>
    <div class="rule rule--title"></div>

    <section class="claim-band">
      <p class="use">use as an adjuvant in case of nausea,<br>vomiting and motion sickness.</p>
      <div class="rule"></div>
      <p class="audience">Ideal for pregnant women</p>
    </section>

    <div class="ginger-visual" role="img" aria-label="Photo of fresh ginger root with sliced pieces and green leaves"></div>
    <div class="organic-seal" role="img" aria-label="Organic certification seal"></div>

    <div class="count">30</div>
    <div class="count-unit">CAPSULES</div>
    <div class="base-tag">BASED ON GINGER</div>
  </main>
</body>
</html>
```